Sales Funnel Infographic

Attached is our sale funnel graphic. We want to rebuild it from scratch as a vector Infographic, preferably .ai file. It will be used on our website & all sales collateral - both web and print.

This is a cornerstone of our marketing to illustrate to our potential clients what we do. We build sales engines for startup companies who don't yet have a department for sales and/or a systematic strategy for sales & marketing.

We will keep the basic funnel design, the copy, the order & relationships - by relationships I mean the arrows/connections between the pieces.

Examples of funnels I like:

http://www.quelvanpost.example/wp-content/uploads/2012/02/inbound-marketing-funnel.jpg

http://www.torvimek.example/~/media/ideas%20blog%20images/video-for-sales-infographic.ashx

http://prandelwystrip.files.hostlane.example/2014/01/3d-funnel-design_01.jpg?w=700

Here's our website: http://grenwhorl.example

our colors: corporate blue: #00144F
font: Titillium Web from Google Fonts

Final size should be 9x16 ratio including white space = tall version of HD widescreen

Target Market(s)

Funded businesses and silicon valley startups who are looking to hire us to create a sales engine for them.

Industry/Entity Type

Marketing

Font styles to use
Sans Serif

Requirements
Must have
• Vector .ai format
Basic Funnel Shape
All copy from attachment & relationships
white background
Nice to have
• optional color background
Should not have
• super-tall format

```html
<!DOCTYPE html>
<html lang="en">
<head>
<meta charset="utf-8">
<title>PRIME Growth Engine – Grenwhorl</title>
<link href="https://fonts.googleapis.com/css2?family=Titillium+Web:wght@400;600;700&display=swap" rel="stylesheet">
<style>
  :root {
    --navy: #163a4f;
    --sub-blue: #3f6f92;
    --band: #183c50;
    --step1: #5b87aa;
    --step1-label: #3a6690;
    --stem: #3d8bcd;
    --stem-light: #c3dbf0;
    --pink: #e8375f;
    --crimson: #c8213f;
    --crimson-dark: #8e1a30;
    --orange: #e07f2a;
    --amber: #f7941d;
    --amber-dark: #d4761c;
    --olive: #c8a43a;
    --green: #1f8c6e;
    --green-dark: #16664f;
    --yellow: #e3c02b;
    --yellow-dark: #c5a42c;
    --ink: #111;
    --white: #fff;
  }
  html, body { margin: 0; padding: 0; overflow: hidden; background: var(--white); }
  .canvas { width: 675px; height: 1200px; position: relative; overflow: hidden; }
  .canvas svg { display: block; }
  text { font-family: "Titillium Web", sans-serif; }
  .title { font-size: 40px; font-weight: 700; fill: var(--navy); }
  .subtitle { font-size: 22px; font-weight: 700; fill: var(--sub-blue); }
  .step { font-size: 19.5px; font-weight: 600; fill: var(--ink); }
  .step-light { fill: var(--white); }
  .label { font-size: 21.5px; font-weight: 400; fill: var(--ink); }
  .label-light { fill: var(--white); }
  .stage { font-size: 30px; font-weight: 400; fill: var(--ink); }
  .stage-sm { font-size: 24px; }
  .money { font-size: 23px; font-weight: 400; fill: var(--ink); }
  .note { font-size: 16px; font-weight: 400; fill: var(--ink); }
  .brand { font-size: 34px; font-weight: 600; fill: var(--navy); }
  .dash { fill: none; stroke: var(--ink); stroke-width: 2; stroke-dasharray: 8 6; }
  .loop { fill: none; stroke: var(--ink); stroke-width: 2.2; }
</style>
</head>
<body>
<div class="canvas">
<svg width="675" height="1200" viewBox="0 0 675 1200" xmlns="http://www.w3.org/2000/svg" aria-labelledby="heading">
  <defs>
    <marker id="arrowhead" viewBox="0 0 12 12" refX="7" refY="6" markerWidth="12" markerHeight="12" orient="auto" markerUnits="userSpaceOnUse">
      <path d="M1 1 L10 6 L1 11" fill="none" stroke="#111" stroke-width="1.8"/>
    </marker>
  </defs>

  <!-- Header -->
  <text id="heading" class="title" x="337.5" y="60" text-anchor="middle">PRIME Growth Engine:</text>
  <text class="subtitle" x="337.5" y="123" text-anchor="middle">A proven process to drive predictable revenue and growth.</text>
  <rect x="0" y="157" width="675" height="16" fill="var(--band)"/>

  <!-- Stem and arrow of the engine -->
  <rect x="358" y="252" width="132" height="245" fill="var(--stem)"/>
  <polygon points="296,495 553,495 424,636" fill="var(--stem)"/>
  <polygon points="318,540 530,540 508,565 340,565" fill="var(--stem-light)"/>
  <text class="label" x="424" y="561" text-anchor="middle">Demand Generation</text>

  <!-- Step 1 -->
  <rect x="0" y="219" width="336" height="34" fill="var(--step1)"/>
  <text class="step step-light" x="26" y="243">1. Clarify vision, goals, values</text>
  <rect x="335" y="219" width="178" height="34" fill="var(--step1-label)"/>
  <text class="label label-light" x="424" y="243" text-anchor="middle">Vision &amp; Goals</text>

  <!-- Step 2 -->
  <rect x="0" y="283" width="280" height="90" fill="var(--pink)"/>
  <text class="step" x="26" y="308">2. Develop, refine audience,</text>
  <text class="step" x="26" y="333">value prop, key messages,</text>
  <text class="step" x="26" y="358">differentiators, channels</text>
  <rect x="280" y="283" width="284" height="34" fill="var(--crimson)"/>
  <text class="label" x="423" y="307" text-anchor="middle">Customer-Centric Strategy</text>

  <!-- Step 3 -->
  <rect x="0" y="392" width="280" height="93" fill="var(--orange)"/>
  <text class="step" x="26" y="418">3. Optimize sales tools,</text>
  <text class="step" x="26" y="443">website, overview, pitch</text>
  <text class="step" x="26" y="468">deck, technologies</text>
  <rect x="280" y="450" width="289" height="35" fill="var(--amber)"/>
  <text class="label" x="424" y="475" text-anchor="middle">Foundational Tools</text>

  <!-- Step 4 -->
  <rect x="0" y="508" width="280" height="93" fill="var(--olive)"/>
  <text class="step" x="26" y="532">4. Prioritize &amp; execute</text>
  <text class="step" x="26" y="557">demand-gen</text>
  <text class="step" x="26" y="582">activities, measure, optimize</text>

  <!-- Funnel: Qualify -->
  <path d="M228 646 Q420 628 612 646 L574 730 Q420 722 268 730 Z" fill="var(--green)"/>
  <path d="M228 646 Q420 628 612 646 Q420 660 228 646 Z" fill="var(--green-dark)"/>
  <text class="stage" x="420" y="697" text-anchor="middle">Qualify</text>

  <!-- Funnel: Develop -->
  <path d="M255 737 Q420 722 585 737 L553 815 Q420 808 283 815 Z" fill="var(--crimson)"/>
  <path d="M255 737 Q420 722 585 737 Q420 750 255 737 Z" fill="var(--crimson-dark)"/>
  <text class="stage" x="420" y="786" text-anchor="middle">Develop</text>

  <!-- Funnel: Close -->
  <path d="M283 824 Q420 810 553 824 L540 893 Q420 886 300 893 Z" fill="var(--amber)"/>
  <path d="M283 824 Q420 810 553 824 Q420 836 283 824 Z" fill="var(--amber-dark)"/>
  <text class="stage" x="420" y="875" text-anchor="middle">Close</text>

  <text class="money" x="414" y="920" text-anchor="middle">$+V</text>

  <!-- Funnel: Growth & Scale -->
  <path d="M310 936 Q420 923 535 936 L515 1001 Q420 995 325 1001 Z" fill="var(--yellow)"/>
  <path d="M310 936 Q420 923 535 936 Q420 947 310 936 Z" fill="var(--yellow-dark)"/>
  <text class="stage stage-sm" x="421" y="982" text-anchor="middle">Growth &amp; Scale</text>

  <text class="money" x="414" y="1043" text-anchor="middle">$$$$$$$$$</text>

  <!-- Steps 5–7 -->
  <text class="step" x="26" y="694">5. Develop, refine,</text>
  <text class="step" x="26" y="719">execute biz dev &amp;</text>
  <text class="step" x="26" y="744">sales process,</text>
  <text class="step" x="26" y="770">account</text>
  <text class="step" x="26" y="796">development,</text>
  <text class="step" x="26" y="822">team</text>

  <text class="step" x="26" y="878">6. Past/current</text>
  <text class="step" x="26" y="903">client relations,</text>
  <text class="step" x="26" y="929">resell,</text>
  <text class="step" x="26" y="955">retention and</text>
  <text class="step" x="26" y="981">referrals, service</text>

  <text class="step" x="26" y="1042">7. Measure, optimize,</text>
  <text class="step" x="26" y="1068">build capacity,</text>
  <text class="step" x="26" y="1094">accelerate, scale</text>

  <!-- Dashed connectors -->
  <path class="dash" d="M258 668 Q225 735 248 790 Q268 838 300 872"/>
  <path class="dash" d="M185 964 L310 964"/>
  <path class="dash" d="M322 920 Q290 945 262 985 Q248 1005 236 1027"/>
  <path class="dash" d="M240 1030 Q300 1048 352 1045"/>

  <!-- Feedback loops -->
  <path class="loop" d="M568 885 Q612 720 594 556" marker-end="url(#arrowhead)"/>
  <path class="loop" d="M522 1035 Q652 990 652 760 Q650 640 598 562"/>
  <path class="loop" d="M522 1035 Q642 990 604 864" marker-end="url(#arrowhead)"/>
  <text class="note" x="570" y="922" text-anchor="middle">Feedback</text>
  <text class="note" x="570" y="943" text-anchor="middle">Loops</text>

  <!-- Brand -->
  <text class="brand" x="337.5" y="1152" text-anchor="middle">Grenwhorl</text>
</svg>
</div>
</body>
</html>
```